Plakat-Design für eine Werbeschild für ein Geflügelhof
Zielgruppe
Wir sind ein Geflügelhof, Landhandel, Hofladen, Eier stehen seit über 100 Jahren für Hof Kranwede, artgerechte Tierhaltung und Artikelvielfalt machen uns bekannt.
Aufgabenstellung
Das Werbeschild wird auf dem Hof aufgestellt und soll den Weg zum Hof zeigen.
- die Maße vom Schild: 1,50m breit x 2,40m hoch
- Grafiken werden als .ai und .pdf benötigt
- Logo ist hochgelagen
- Foto von unserer Vorstellung ist hochgeladen
Das Schild muss 400 m RECHTS drauf gedruckt haben.
Falls es zu breit wäre, könnte das Logo ja vielleicht auch über Hof Kranwede.
Das ganze wird bei plattenwerk auf eine MetoxPan-Platte in den Druck gegeben.

```html
<!DOCTYPE html>
<html lang="de">
<head>
<meta charset="utf-8">
<title>Hof Kranwede – Einkauf auf dem Bauernhof</title>
<link href="https://fonts.googleapis.com/css2?family=Amatic+SC:wght@400;700&display=swap" rel="stylesheet">
<style>
  :root {
    --backdrop: #e6e6e3;
    --sign-cream: #f4f0d8;
    --farm-green: #2e8a44;
    --signal-pink: #e8295a;
    --chick-yellow: #f6cf3c;
    --chick-warm: #eeb52c;
    --bike-teal: #2f8a78;
  }
  html, body {
    margin: 0;
    width: 1200px;
    height: 763px;
    overflow: hidden;
    background: var(--backdrop);
  }
  .canvas {
    position: relative;
    width: 1200px;
    height: 763px;
  }
  .sign {
    position: absolute;
    left: 381px;
    top: 31px;
    width: 438px;
    height: 700px;
    background: var(--sign-cream);
    box-shadow: 0 2px 10px rgba(0,0,0,0.15);
    font-family: "Amatic SC", "Arial Narrow", sans-serif;
    color: var(--farm-green);
  }
  .brand {
    position: absolute;
    top: 26px;
    left: 32px;
    display: flex;
    align-items: center;
    gap: 12px;
  }
  .brand-dot {
    width: 46px;
    height: 46px;
    border-radius: 50%;
    background: var(--farm-green);
  }
  .brand-name {
    font-weight: 700;
    font-size: 40px;
    line-height: 1;
  }
  .headline {
    position: absolute;
    top: 120px;
    left: 0;
    width: 100%;
    text-align: center;
    font-weight: 700;
    line-height: 0.9;
    margin: 0;
  }
  .headline-main {
    display: block;
    font-size: 112px;
  }
  .headline-small {
    display: block;
    font-size: 44px;
    margin: 4px 0 2px;
  }
  .mini-chick {
    position: absolute;
    top: 150px;
    right: 28px;
    width: 50px;
    height: 64px;
    border-radius: 45% 45% 40% 40%;
    background: linear-gradient(160deg, var(--chick-yellow), var(--chick-warm));
  }
  .bike-chick {
    position: absolute;
    left: 8px;
    bottom: 24px;
    width: 200px;
    height: 255px;
    border-radius: 40% 40% 20% 20%;
    background: linear-gradient(180deg, var(--chick-yellow) 0%, var(--chick-warm) 65%, var(--bike-teal) 100%);
  }
  .direction {
    position: absolute;
    left: 200px;
    top: 440px;
    display: flex;
    align-items: center;
    gap: 8px;
    color: var(--signal-pink);
  }
  .direction-arrow {
    width: 80px;
    height: 56px;
    margin-top: 40px;
  }
  .direction-text {
    text-align: center;
    line-height: 0.9;
    font-weight: 700;
  }
  .distance {
    display: block;
    font-size: 78px;
  }
  .distance small {
    font-size: 44px;
  }
  .turn {
    display: block;
    font-size: 40px;
  }
</style>
</head>
<body>
<div class="canvas">
  <div class="sign">
    <div class="brand">
      <span class="brand-dot"></span>
      <span class="brand-name">Hof Kranwede</span>
    </div>

    <h1 class="headline">
      <span class="headline-main">Einkauf</span>
      <span class="headline-small">auf dem</span>
      <span class="headline-main">Bauernhof</span>
    </h1>

    <div class="mini-chick" role="img" aria-label="Kleines gezeichnetes Küken mit Stock"></div>

    <div class="bike-chick" role="img" aria-label="Gezeichnetes gelbes Huhn auf einem grünen Fahrrad"></div>

    <div class="direction">
      <svg class="direction-arrow" viewBox="0 0 80 56" aria-hidden="true">
        <path d="M0 20 H48 V4 L80 28 L48 52 V36 H0 Z" fill="var(--signal-pink)"/>
      </svg>
      <div class="direction-text">
        <span class="distance">400<small>m</small></span>
        <span class="turn">Rechts</span>
      </div>
    </div>
  </div>
</div>
</body>
</html>
```